Carpentry company Needs a business card design

We need a design for a Carpentry / building company, business card. Please think of designs out of the ordinary and try to make it eye catching. Our existing logo will need to be incorporated in the design. However feel free to change the colours of the logo to suit your design. I would like to see some designs with green /black and orange incorporated into it.These are not the only colours accepted and all designs that appeal will be accepted.

Please contact me should you have any questions
Thanks Martin

Target Market(s)

General Public seeking carpentry work

Industry/Entity Type

Business

Contact Information for Business Card

- Current company logo ( colours can be changed)
-Phone number ,
- info@brelvanbuild.com.au
- brelvanbuild.com.au
-the facebook symbol

Font styles to use
Other font styles liked:
• You choose

Requirements
Must have
• Services we provide
• - Renovations
• -Deckings & Pergolas
• -Kitchens
• - Bathrooms
• - Intricate details
Nice to have
• an awesome design
Should not have
• Tools on the business card

```html
<!DOCTYPE html>
<html lang="en">
<head>
<meta charset="utf-8">
<title>Brelvan Build – Business Card</title>
<link href="https://fonts.googleapis.com/css2?family=Open+Sans:wght@400;600;700&display=swap" rel="stylesheet">
<style>
  :root {
    --backdrop: #e9e6e2;
    --card: #ffffff;
    --ink: #1a1a1a;
    --brand-dark: #2a1d18;
    --copper: #c98a3c;
    --band-orange: #d3882e;
  }
  * { margin: 0; padding: 0; box-sizing: border-box; }
  html, body { width: 1200px; height: 1000px; overflow: hidden; }
  body {
    background: var(--backdrop);
    font-family: "Open Sans", Arial, sans-serif;
    color: var(--ink);
    position: relative;
  }
  .card {
    position: absolute;
    left: 265px;
    width: 665px;
    height: 397px;
    background: var(--card);
    box-shadow: 0 2px 8px rgba(0,0,0,0.25);
    overflow: hidden;
  }
  .card--front { top: 73px; }
  .card--back { top: 532px; }

  .brand {
    position: absolute;
    display: flex;
    align-items: center;
    color: var(--brand-dark);
    font-weight: 700;
    letter-spacing: 1px;
    text-transform: uppercase;
  }
  .brand__square { background: var(--copper); flex: none; }
  .card--front .brand { left: 33px; top: 112px; font-size: 40px; gap: 12px; transform: translateY(-50%); }
  .card--front .brand__square { width: 18px; height: 18px; }
  .card--back .brand { left: 0; right: 0; top: 183px; justify-content: center; font-size: 52px; gap: 16px; transform: translateY(-50%); }
  .card--back .brand__square { width: 22px; height: 22px; }

  .services {
    position: absolute;
    right: 32px;
    top: 42px;
    list-style: none;
    text-align: right;
    font-size: 16px;
    line-height: 23.6px;
  }
  .services li { display: flex; justify-content: flex-end; align-items: center; gap: 6px; }
  .services svg { width: 14px; height: 14px; }

  .person {
    position: absolute;
    left: 33px; right: 32px;
    top: 226px;
    border-bottom: 1.5px solid var(--ink);
    text-align: right;
    padding-bottom: 2px;
  }
  .person__name { color: var(--copper); font-weight: 700; font-size: 22px; }
  .person__role { position: absolute; right: 32px; top: 264px; font-size: 16px; }

  .contacts {
    position: absolute;
    left: 33px; top: 280px;
    list-style: none;
    font-size: 16px;
    line-height: 25.5px;
  }
  .contacts li { display: flex; align-items: center; gap: 7px; }
  .contacts svg { width: 16px; height: 16px; flex: none; }

  .footer-bands { position: absolute; left: 0; bottom: 0; width: 665px; height: 35px; }
  .footer-url {
    position: absolute; right: 32px; bottom: 8px;
    color: #fff; font-size: 17px; letter-spacing: 1.6px;
  }

  .back-url {
    position: absolute; left: 0; right: 0; top: 346px;
    text-align: center; font-size: 18px; color: var(--brand-dark);
  }
  .back-url__name { color: var(--copper); }
</style>
</head>
<body>

<section class="card card--front">
  <div class="brand"><span class="brand__square"></span>Brelvan Build</div>

  <ul class="services">
    <li>Renovations <svg viewBox="0 0 14 14"><path d="M7 1 13 7 7 13 1 7Z" fill="var(--brand-dark)"/><path d="M7 4.5 9.5 7 7 9.5 4.5 7Z" fill="var(--copper)"/></svg></li>
    <li>Deckings &amp; Pergolas <svg viewBox="0 0 14 14"><path d="M7 1 13 7 7 13 1 7Z" fill="var(--brand-dark)"/><path d="M7 4.5 9.5 7 7 9.5 4.5 7Z" fill="var(--copper)"/></svg></li>
    <li>Kitchens <svg viewBox="0 0 14 14"><path d="M7 1 13 7 7 13 1 7Z" fill="var(--brand-dark)"/><path d="M7 4.5 9.5 7 7 9.5 4.5 7Z" fill="var(--copper)"/></svg></li>
    <li>Bathrooms <svg viewBox="0 0 14 14"><path d="M7 1 13 7 7 13 1 7Z" fill="var(--brand-dark)"/><path d="M7 4.5 9.5 7 7 9.5 4.5 7Z" fill="var(--copper)"/></svg></li>
    <li>Intricate details <svg viewBox="0 0 14 14"><path d="M7 1 13 7 7 13 1 7Z" fill="var(--brand-dark)"/><path d="M7 4.5 9.5 7 7 9.5 4.5 7Z" fill="var(--copper)"/></svg></li>
  </ul>

  <div class="person"><span class="person__name">Martin Hartley</span></div>
  <div class="person__role">Director</div>

  <ul class="contacts">
    <li><svg viewBox="0 0 16 16"><rect width="16" height="16" fill="var(--copper)"/></svg>brelvanbuild</li>
    <li><svg viewBox="0 0 16 16"><rect width="16" height="16" fill="var(--copper)"/><path d="M4 5c0-1 1-1.5 4-1.5S12 4 12 5v1h-2V5.2H6V6H4Z M5 8h6l1 4H4Z" fill="#fff"/></svg>000 000 0000</li>
    <li><svg viewBox="0 0 16 16"><rect width="16" height="16" fill="var(--copper)"/><rect x="3" y="4.5" width="10" height="7" fill="none" stroke="#fff" stroke-width="1.2"/><path d="M3 4.5 8 8.5 13 4.5" fill="none" stroke="#fff" stroke-width="1.2"/></svg>info@brelvanbuild.com.au</li>
  </ul>

  <svg class="footer-bands" viewBox="0 0 665 35" preserveAspectRatio="none">
    <polygon points="0,17 373,17 357,35 0,35" fill="var(--band-orange)"/>
    <polygon points="398,0 665,0 665,35 366,35" fill="var(--ink)"/>
  </svg>
  <div class="footer-url">brelvanbuild.com.au</div>
</section>

<section class="card card--back">
  <div class="brand"><span class="brand__square"></span>Brelvan Build</div>
  <div class="back-url">www.<span class="back-url__name">brelvanbuild</span>.com.au</div>
</section>

</body>
</html>
```